Business Card and Letterhead for Nurlo - modern real estate business

I need a double sided business card design for Nurlo. Please see business card brief here https://papers.trelvimo.net/sheet/q/7XrTbaLeZpMmQ2uWvd9HkCj4yNoEfsGi3lRtAz_pk/view?mode=shared

Please feel free to design the business cards however you feel best. I am happy to give some creative freedoms and then provide feedback from there.

Please then also create a letterhead to match the business card design

Colors

Designer to choose colors to be used in the design.

Requirements
Must have
• Must be a modern, elegant business card which looks very professional

```html
<!DOCTYPE html>
<html lang="en">
<head>
<meta charset="utf-8">
<title>Nurlo Business Card</title>
<link rel="stylesheet" href="https://fonts.googleapis.com/css2?family=Archivo:wght@500;600;700&display=swap">
<style>
  :root {
    --brand-red: #e3101e;
    --ink: #1b1b1b;
    --card-black: #050505;
    --card-black-glow: #151515;
    --paper: #ffffff;
    --backdrop: #2a2a2c;
    --portrait-dark: #222224;
    --portrait-mid: #4a4a4e;
  }
  * { box-sizing: border-box; margin: 0; padding: 0; }
  html, body {
    width: 1200px;
    height: 736px;
    overflow: hidden;
    background: var(--backdrop);
    font-family: "Archivo", Arial, sans-serif;
  }
  .sheet {
    position: relative;
    width: 1200px;
    height: 736px;
  }
  .card {
    position: absolute;
    top: 210px;
    width: 540px;
    height: 316px;
    border-radius: 16px;
    overflow: hidden;
    border-right: 4px solid var(--brand-red);
    border-bottom: 4px solid var(--brand-red);
    box-shadow: 0 14px 30px rgba(0,0,0,0.45);
  }

  /* Back side */
  .card--back {
    left: 40px;
    background: radial-gradient(circle at 50% 50%, var(--card-black-glow) 0%, var(--card-black) 70%);
    display: flex;
    align-items: center;
    justify-content: center;
  }
  .brand-name {
    color: var(--brand-red);
    font-weight: 600;
    font-size: 66px;
    letter-spacing: 6px;
    text-transform: uppercase;
  }

  /* Front side */
  .card--front {
    left: 620px;
    background: var(--paper);
  }
  .accent-bar {
    position: absolute;
    left: 0;
    top: 104px;
    width: 10px;
    height: 62px;
    background: var(--brand-red);
  }
  .agent {
    position: absolute;
    left: 34px;
    top: 102px;
  }
  .agent__name {
    color: var(--brand-red);
    font-weight: 700;
    font-size: 24px;
    letter-spacing: 0.5px;
    text-transform: uppercase;
    line-height: 1.05;
  }
  .agent__role,
  .agent__licence {
    color: var(--ink);
    font-weight: 500;
    font-size: 13px;
    line-height: 1.35;
  }
  .contact {
    position: absolute;
    left: 56px;
    bottom: 36px;
    list-style: none;
  }
  .contact__item {
    display: flex;
    align-items: center;
    gap: 10px;
    color: var(--ink);
    font-weight: 600;
    font-size: 16px;
    line-height: 1.55;
  }
  .contact__icon {
    width: 13px;
    height: 13px;
    flex: none;
  }
  .portrait {
    position: absolute;
    right: 0;
    bottom: 0;
    width: 262px;
    height: 268px;
    background: linear-gradient(180deg, var(--portrait-mid) 0%, var(--portrait-dark) 45%, #141416 100%);
    border-radius: 120px 120px 0 0;
  }
</style>
</head>
<body>
<main class="sheet">

  <section class="card card--back" aria-label="Card back">
    <span class="brand-name">Nurlo</span>
  </section>

  <section class="card card--front" aria-label="Card front">
    <div class="accent-bar"></div>
    <div class="agent">
      <h1 class="agent__name">Mason Trell</h1>
      <p class="agent__role">Licenced Real Estate Agent</p>
      <p class="agent__licence">Lic No. 20318846</p>
    </div>

    <ul class="contact">
      <li class="contact__item">
        <svg class="contact__icon" viewBox="0 0 24 24" aria-hidden="true">
          <path fill="#e3101e" d="M6.6 10.8a15.1 15.1 0 0 0 6.6 6.6l2.2-2.2a1 1 0 0 1 1-.25 11.4 11.4 0 0 0 3.6.57 1 1 0 0 1 1 1V20a1 1 0 0 1-1 1A17 17 0 0 1 3 4a1 1 0 0 1 1-1h3.5a1 1 0 0 1 1 1c0 1.25.2 2.45.57 3.6a1 1 0 0 1-.25 1z"/>
        </svg>
        0412 368 905
      </li>
      <li class="contact__item">
        <svg class="contact__icon" viewBox="0 0 24 24" aria-hidden="true">
          <g fill="none" stroke="#e3101e" stroke-width="2.2">
            <circle cx="12" cy="12" r="9.5"/>
            <ellipse cx="12" cy="12" rx="4.2" ry="9.5"/>
            <path d="M2.5 12h19M4 7h16M4 17h16"/>
          </g>
        </svg>
        mason@nurlo.com
      </li>
    </ul>

    <div class="portrait" role="img" aria-label="Portrait photo of the agent in a dark suit"></div>
  </section>

</main>
</body>
</html>
```